Cosmetic injections clinic needs a fresh looking business card

We need a business card using the supplied logo and color scheme to attract future clients to our clinic. It should be modern and fresh, eye catching and not too busy. Simple and to the point is best. I would like two sided designs with the front indicating address and contact information, and the back in full color with white logo and descriptive information also provided.
Target Market(s)
Clients looking for non surgical beauty enhancements.
Contact Information for Business Card
MeloraSkin
14, 618 Birchmont Way
St. Albert, Alberta
K2P 7W3
Phone: 587-412-6630
Email: info@meloraskin.com
Requirements
Must have
- -Logo supplied with the name and address of the clinic
- -Back of card in full color with white logo with A small line of text indicating both of the following: Anti aging consultants and cosmetic injectables
- Located inside the Voyager Wellness Group

```html
<!DOCTYPE html>
<html lang="en">
<head>
<meta charset="utf-8">
<title>MeloraSkin business card</title>
<link href="https://fonts.googleapis.com/css2?family=Lato:wght@400;700&family=Raleway:wght@400;500&display=swap" rel="stylesheet">
<style>
  :root {
    --teal: #26b9a7;
    --purple: #5b3c98;
    --pink: #e5409a;
    --ink: #1d1d1f;
    --paper: #ffffff;
    --backdrop: #2a2a2c;
  }
  * { box-sizing: border-box; margin: 0; padding: 0; }
  html, body { width: 1200px; height: 950px; overflow: hidden; }
  body { background: var(--backdrop); position: relative; font-family: "Lato", sans-serif; }

  .card {
    position: absolute;
    width: 700px;
    height: 400px;
    box-shadow: 0 18px 40px rgba(0,0,0,0.45);
  }

  /* Back side */
  .card-back { left: 150px; top: 50px; background: var(--teal); color: var(--paper); }
  .card-back .wordmark {
    position: absolute; left: 380px; top: 150px;
    display: flex; align-items: center; gap: 14px;
  }
  .card-back .wordmark-dot { width: 44px; height: 44px; border-radius: 50%; background: var(--paper); }
  .card-back .wordmark-name {
    font-family: "Lato", sans-serif; font-weight: 700; font-size: 42px; color: var(--paper);
  }
  .card-back .tagline {
    position: absolute; left: 380px; top: 214px; width: 300px;
    font-family: "Raleway", sans-serif; font-size: 16px; line-height: 1.35; letter-spacing: 0.3px;
  }

  /* Front side */
  .card-front { left: 350px; top: 500px; background: var(--paper); color: var(--ink); }
  .card-front .wordmark {
    position: absolute; right: 60px; top: 70px;
    display: flex; align-items: center; gap: 14px;
  }
  .card-front .wordmark-dot { width: 44px; height: 44px; border-radius: 50%; background: var(--purple); }
  .card-front .wordmark-name { font-weight: 700; font-size: 40px; color: var(--purple); }

  .contact-list { position: absolute; left: 60px; top: 180px; list-style: none; }
  .contact-list li { display: flex; align-items: center; gap: 12px; font-size: 19px; margin-bottom: 10px; }
  .contact-list svg { width: 24px; height: 24px; }

  .divider { position: absolute; left: 60px; top: 262px; width: 340px; height: 2px; background: var(--ink); }

  .address { position: absolute; left: 60px; top: 278px; font-style: normal; }
  .address .clinic-name { font-size: 26px; color: var(--purple); margin-bottom: 2px; }
  .address p { font-size: 17px; line-height: 1.25; }
</style>
</head>
<body>

  <section class="card card-back" aria-label="Card back">
    <div class="wordmark">
      <span class="wordmark-dot"></span>
      <span class="wordmark-name">MeloraSkin</span>
    </div>
    <p class="tagline">Anti aging consultants and cosmetic injectables</p>
  </section>

  <section class="card card-front" aria-label="Card front">
    <div class="wordmark">
      <span class="wordmark-dot"></span>
      <span class="wordmark-name">MeloraSkin</span>
    </div>

    <ul class="contact-list">
      <li>
        <svg viewBox="0 0 24 24" aria-hidden="true"><circle cx="12" cy="12" r="10.5" fill="none" stroke="#1d1d1f" stroke-width="1.8"/><path d="M8.5 7.5c.6-.6 1.3-.5 1.7.1l1 1.5c.3.5.2 1-.2 1.4l-.6.5c.6 1.3 1.6 2.3 2.9 2.9l.5-.6c.4-.4.9-.5 1.4-.2l1.5 1c.6.4.7 1.1.1 1.7-1.3 1.3-3.4.9-5.5-1.2s-3-4.3-1.8-5.5z" fill="#1d1d1f"/></svg>
        <span>: 587-412-6630</span>
      </li>
      <li>
        <svg viewBox="0 0 24 24" aria-hidden="true"><rect x="2" y="5" width="20" height="14" fill="#1d1d1f"/><path d="M2 5l10 8 10-8M2 19l7-7M22 19l-7-7" fill="none" stroke="#fff" stroke-width="1.4"/></svg>
        <span>: info@meloraskin.com</span>
      </li>
    </ul>

    <div class="divider"></div>

    <address class="address">
      <p class="clinic-name">MeloraSkin</p>
      <p>14, 618 Birchmont Way</p>
      <p>St. Albert, Alberta</p>
      <p>K2P 7W3</p>
    </address>
  </section>

</body>
</html>
```